M Website

We need a website design for a construction plant company. You may use a combination of our photos and the stock images. See the logo for company colours. It also be of great value to see moving pictures like the ones on the link: https://www.quindellworks.co.za/copy-of-about-us. See our uploaded files for content.

Target Market(s)

Construction

Number of Pages Required

5+ page

```html
<!DOCTYPE html>
<html lang="en">
<head>
<meta charset="utf-8">
<title>Harbrook Plant and Civils</title>
<link href="https://fonts.googleapis.com/css2?family=Lato:wght@300;400;700;900&display=swap" rel="stylesheet">
<style>
:root{
  --bg:#2c2c2c;
  --bg-dark:#232323;
  --bg-band:#1f1f1f;
  --accent:#f6b817;
  --text:#ffffff;
  --muted:#a9a9a9;
  --ghost:rgba(255,255,255,0.05);
}
*{margin:0;padding:0;box-sizing:border-box}
html,body{width:1200px;height:5014px;overflow:hidden}
body{background:var(--bg);color:var(--text);font-family:"Lato",sans-serif;position:relative}
.sec{position:absolute;left:0;width:1200px}
.abs{position:absolute}
.heading{font-size:32px;font-weight:700;text-align:center;width:100%}
.heading span{color:var(--accent)}
.ghost{font-size:80px;font-weight:700;color:var(--ghost);text-align:center;width:100%;letter-spacing:2px}
.view-more{font-size:14px;color:var(--accent);text-align:center;width:100%}
.view-more::after{content:" \2192"}
.photo{position:absolute}

.hero{top:0;height:500px;background:linear-gradient(180deg,#3a3733 0%,#4b4740 45%,#5b6472 75%,#2c2c2c 100%)}
.nav{position:absolute;top:0;left:0;width:1200px;height:47px;display:flex;align-items:center}
.brand{position:absolute;left:150px;top:8px;display:flex;align-items:center;gap:8px;font-weight:900;font-size:18px;color:var(--accent)}
.brand i{width:22px;height:22px;background:var(--accent);display:block}
.menu{position:absolute;left:465px;top:17px;display:flex;gap:58px;font-size:13px;color:#ddd}
.menu .on{color:var(--accent);border-bottom:2px solid var(--accent);padding-bottom:4px}
.hero-box{left:425px;top:134px;width:350px;height:233px;background:rgba(40,40,40,.55)}
.hero-frame{left:474px;top:160px;width:260px;height:185px;border:3px solid #fff;border-right:none}
.hero-title{left:488px;top:185px;font-size:29px;font-weight:700;line-height:48px}
.hero-play{left:588px;top:395px;width:26px;height:26px;border-radius:50%;background:var(--accent)}
.side-tab{right:0;top:180px;width:30px;height:180px;background:#1d1d1d;color:var(--accent);font-size:11px;writing-mode:vertical-rl;display:flex;align-items:center;justify-content:center;letter-spacing:3px}

.about{top:500px;height:570px}
.about-frame{left:150px;top:110px;width:200px;height:160px;border-left:4px solid var(--accent);border-top:4px solid var(--accent)}
.about .photo{left:167px;top:128px;width:368px;height:365px;background:linear-gradient(180deg,#7fa1c4 0%,#c7b98e 55%,#8a7658 100%)}
.about-title{left:560px;top:105px;font-size:32px;font-weight:700}
.about-title span{color:var(--accent)}
.about-text{left:560px;top:170px;width:500px;font-size:11.5px;line-height:19px;color:var(--muted)}
.ticks{left:560px;top:300px;font-size:11px;color:#ddd;display:flex;gap:22px}
.ticks b{color:var(--accent)}
.mission{left:560px;top:340px;font-size:15px;font-weight:700}
.mission span{color:var(--accent)}
.mission-text{left:560px;top:372px;width:500px;font-size:11.5px;line-height:19px;color:var(--muted)}
.read-more{left:930px;top:505px;font-size:14px;color:var(--accent)}
.read-more::after{content:" \2192"}

.enquiry{top:1085px;height:170px;background:linear-gradient(180deg,#2c2c2c,#3c3e42 60%,#2c2c2c)}
.enquiry-text{left:230px;top:70px;font-size:24px;font-weight:700}
.btn-light{left:848px;top:68px;width:125px;height:34px;background:#fff;color:#222;font-size:13px;display:flex;align-items:center;justify-content:center}
.btn-light::after{content:"\00a0\2192"}

.services{top:1250px;height:870px}
.services .ghost{top:0}
.services .heading{top:92px}
.sub{font-size:13px;color:var(--muted);text-align:center;width:100%;line-height:20px}
.services .sub{top:150px}
.tile-label{position:absolute;bottom:40px;width:100%;text-align:center;font-size:14px;line-height:20px}
.featured{background:rgba(20,20,20,.92)}
.feat-frame{position:absolute;border:3px solid var(--accent)}
.vert{position:absolute;writing-mode:vertical-rl;transform:rotate(180deg);font-size:12px;color:#ddd;letter-spacing:1px}
.zoom{position:absolute;width:36px;height:36px}
.services .view-more{top:772px}

.news{top:2110px;height:260px}
.news .ghost{top:0}
.news .heading{top:68px}
.news-input{left:350px;top:168px;width:380px;height:36px;background:#222;color:#777;font-size:12px;padding:11px 14px}
.news-btn{left:730px;top:168px;width:115px;height:36px;background:var(--accent);color:#222;font-size:12px;display:flex;align-items:center;justify-content:center}

.portfolio{top:2370px;height:900px}
.portfolio .ghost{top:0}
.portfolio .heading{top:72px}
.portfolio .view-more{top:858px}

.team{top:3290px;height:700px}
.team .ghost{top:0}
.team .heading{top:86px}
.card{position:absolute;top:192px;width:285px;height:322px;background:#1e1e1e}
.card .photo{left:0;top:0;width:285px;height:322px}
.card-tag{position:absolute;left:0;bottom:18px;background:var(--accent);color:#222;font-size:10px;padding:6px 14px}
.card-role{position:absolute;bottom:12px;width:100%;text-align:center;font-size:11px}
.corner{position:absolute;width:0;height:0}
.team .view-more{top:602px}
.arrows{position:absolute;font-size:30px;color:#ddd;letter-spacing:10px}

.stats{top:3985px;height:90px;display:flex}
.stat{position:absolute;text-align:center;width:160px}
.stat b{display:block;font-size:26px;color:var(--accent);font-weight:700}
.stat span{font-size:13px;color:#ddd}

.testi{top:4140px;height:470px}
.testi .ghost{top:0}
.testi .heading{top:58px}
.avatar{left:575px;top:150px;width:66px;height:66px;border-radius:50%;background:linear-gradient(180deg,#b8a58c,#6e5c4c)}
.testi-name{top:238px;width:100%;text-align:center;font-size:14px;font-weight:700}
.testi .sub{top:272px;left:400px;width:400px;font-size:11.5px;line-height:19px}
.quote{font-size:170px;font-family:Georgia,serif;color:#555;line-height:1}

.contact{top:4600px;height:380px}
.contact .ghost{top:0}
.contact .heading{top:84px}
.col{position:absolute;top:160px;width:300px}
.col h4{text-align:center;color:var(--accent);font-size:13px;font-weight:700;margin-bottom:16px}
.col p{font-size:11.5px;line-height:21px;color:#ccc;text-align:center}
.row{display:flex;align-items:center;gap:10px;font-size:11.5px;color:#ccc;margin-bottom:12px}
.row i{width:24px;height:24px;border:1px solid var(--accent);border-radius:50%;display:block}
.divider{position:absolute;top:172px;width:1px;height:160px;background:#444}

.footer{top:4982px;height:32px;background:var(--bg-band);font-size:10px;color:#999}
.footer .social{display:flex;gap:8px}
.footer .social i{width:20px;height:20px;background:#3a3a3a;display:block}
</style>
</head>
<body>

<header class="sec hero">
  <div class="nav">
    <div class="brand"><i></i>Harbrook</div>
    <nav class="menu"><span class="on">Home</span><span>About Us</span><span>Our Services</span><span>Portfolio</span><span>Our Team</span><span>Contact Us</span></nav>
  </div>
  <div class="photo" style="left:0;top:0;width:1200px;height:500px;background:linear-gradient(180deg,rgba(30,28,25,.7) 0%,rgba(70,68,64,.3) 40%,rgba(100,120,140,.4) 70%,rgba(44,44,44,1) 100%)" role="img" aria-label="City skyline under construction with cranes at dusk"></div>
  <div class="abs hero-box"></div>
  <div class="abs hero-frame"></div>
  <h1 class="abs hero-title">Transforming<br>Our Clients Vision<br>Into Reality</h1>
  <div class="abs hero-play"></div>
  <div class="abs side-tab">CONTACT US</div>
</header>

<section class="sec about">
  <div class="abs about-frame"></div>
  <div class="photo" role="img" aria-label="Two men standing beside yellow backhoe loaders on site"></div>
  <h2 class="abs about-title">About <span>Us</span></h2>
  <p class="abs about-text">Harbrook Plant and Civils (Pty) Ltd is a Black Women owned Construction and Plant Hire company operating mainly from the Kestrel Park area. Harbrook has grown from a small fleet into a trusted contractor serving public and private clients across the region, offering earthworks, roads and bulk services with skilled teams, reliable machines and a strong focus on safety, quality and delivery on time.</p>
  <div class="abs ticks"><span><b>&#10003;</b> Roads &amp; Stormwater</span><span><b>&#10003;</b> Water infrastructure</span><span><b>&#10003;</b> Sanitation infrastructure and housing</span></div>
  <h3 class="abs mission">Mission <span>Statement</span></h3>
  <p class="abs mission-text">Harbrook Plant and Civils aims to employ the professional skills of its staff to deliver quality projects and sustainable engineering solutions, adding value to clients and to the growth of local communities, so that every client is proud to return to us for new work.</p>
  <a class="abs read-more">Read More</a>
</section>

<section class="sec enquiry">
  <p class="abs enquiry-text">Please send all enquiries to:&nbsp; info@harbrookplant.co.za</p>
  <a class="abs btn-light">Contact Us</a>
</section>

<section class="sec services">
  <div class="abs ghost">Overall Offering</div>
  <h2 class="abs heading">Our <span>Services</span></h2>
  <p class="abs sub">Harbrook Plant and Civils (Pty) Ltd has expertise in the following key fields and has successfully executed<br>projects in each of them.</p>
  <div class="photo" style="left:0;top:280px;width:300px;height:410px;background:linear-gradient(160deg,#8a8a8a,#3a3a3a)" role="img" aria-label="Concrete arch colonnade"><div class="tile-label">Structural Concrete<br>Construction</div></div>
  <div class="photo" style="left:300px;top:280px;width:283px;height:410px;background:linear-gradient(180deg,#8aa7c4 0%,#6d7d55 45%,#333 100%)" role="img" aria-label="Road paving with asphalt roller"><div class="tile-label">Structural Concrete<br>Construction</div></div>
  <div class="photo featured" style="left:583px;top:255px;width:333px;height:460px">
    <div class="feat-frame" style="left:80px;top:30px;width:195px;height:395px"></div>
    <div class="abs" style="left:0;top:55px;width:333px;text-align:center;font-size:14px;line-height:20px">Structural Concrete<br>Construction</div>
    <svg class="zoom" style="left:148px;top:205px" viewBox="0 0 36 36"><circle cx="15" cy="15" r="10" fill="none" stroke="#fff" stroke-width="2.5"/><line x1="22" y1="22" x2="32" y2="32" stroke="#fff" stroke-width="3"/><line x1="10" y1="15" x2="20" y2="15" stroke="#fff" stroke-width="2"/><line x1="15" y1="10" x2="15" y2="20" stroke="#fff" stroke-width="2"/></svg>
    <div class="vert" style="left:42px;top:120px">Harbrook Plant &amp; Civils</div>
  </div>
  <div class="photo" style="left:916px;top:280px;width:284px;height:410px;background:linear-gradient(180deg,#9fb9d4 0%,#7f8a92 45%,#4a5560 100%)" role="img" aria-label="Water treatment works"><div class="tile-label">Structural Concrete<br>Construction</div></div>
  <a class="abs view-more">View More</a>
</section>

<section class="sec news">
  <div class="abs ghost">Newsletter</div>
  <h2 class="abs heading">Subscribe Our <span>Newsletter</span></h2>
  <div class="abs news-input">Enter Your Email</div>
  <a class="abs news-btn">Subscribe</a>
</section>

<section class="sec portfolio">
  <div class="abs ghost">Our Portfolio</div>
  <h2 class="abs heading">Our <span>Portfolio</span></h2>
  <div class="photo" style="left:0;top:197px;width:267px;height:295px;background:linear-gradient(180deg,#a79a88,#6e6050)" role="img" aria-label="Worker drilling on a trench site"></div>
  <div class="photo featured" style="left:267px;top:170px;width:368px;height:322px;background:rgba(30,30,30,.95)">
    <div class="feat-frame" style="left:35px;top:30px;width:270px;height:260px"></div>
    <svg class="zoom" style="left:156px;top:85px" viewBox="0 0 36 36"><circle cx="15" cy="15" r="10" fill="none" stroke="#fff" stroke-width="2.5"/><line x1="22" y1="22" x2="32" y2="32" stroke="#fff" stroke-width="3"/></svg>
    <div class="abs" style="left:35px;top:140px;width:270px;text-align:center;font-size:13px;line-height:20px;color:#ddd">Project Name<br>Click The Zoom Button For<br>More Details For The Project</div>
    <div class="vert" style="left:318px;top:60px">Harbrook Plant &amp; Civils</div>
  </div>
  <div class="photo" style="left:635px;top:197px;width:261px;height:295px;background:linear-gradient(180deg,#8d7d62,#5f6b3e)" role="img" aria-label="Crew working in an excavation"></div>
  <div class="photo" style="left:896px;top:197px;width:304px;height:295px;background:linear-gradient(180deg,#9ec0e0 0%,#6c8d4c 55%,#333 100%)" role="img" aria-label="Asphalt paving crew on a road"></div>
  <div class="photo" style="left:0;top:492px;width:300px;height:298px;background:linear-gradient(180deg,#a6bfd8 0%,#5a5a5a 55%,#2a2a2a 100%)" role="img" aria-label="Paving machine with worker"></div>
  <div class="photo" style="left:300px;top:492px;width:300px;height:298px;background:linear-gradient(180deg,#8c6a48,#4f86b4 60%,#7a5a3c)" role="img" aria-label="Blue pipeline laid in a trench"></div>
  <div class="photo" style="left:600px;top:492px;width:300px;height:298px;background:linear-gradient(180deg,#a7b8c6,#c9b98a 55%,#6d6a55)" role="img" aria-label="Tipper truck offloading on site"></div>
  <div class="photo" style="left:900px;top:492px;width:300px;height:298px;background:linear-gradient(180deg,#7e6d4e,#324a8a 55%,#5a4a38)" role="img" aria-label="Workers in overalls digging"></div>
  <a class="abs view-more">View More</a>
</section>

<section class="sec team">
  <div class="abs ghost">Meet Our Team</div>
  <h2 class="abs heading">Our <span>Team</span></h2>
  <div class="card" style="left:150px">
    <div class="photo" style="background:linear-gradient(180deg,#c7b4a4,#5a3a3a)" role="img" aria-label="Portrait of the director"></div>
    <div class="card-tag">Director</div>
  </div>
  <div class="card" style="left:458px">
    <svg class="corner" style="left:0;top:0;width:60px;height:60px" viewBox="0 0 60 60"><polygon points="0,0 60,0 0,60" fill="#f6b817"/></svg>
    <svg class="corner" style="right:0;bottom:0;width:60px;height:60px" viewBox="0 0 60 60"><polygon points="60,0 60,60 0,60" fill="#f6b817"/></svg>
    <div class="abs" style="left:0;top:60px;width:285px;text-align:center;font-size:12px;font-weight:700">TOMAS NDLARO</div>
    <div class="abs" style="left:0;top:80px;width:285px;text-align:center;font-size:10px;color:var(--accent)">Advisor | Consulting</div>
    <div class="abs" style="left:40px;top:110px;width:205px;text-align:center;font-size:10px;line-height:16px;color:#bbb">Civil engineer, Consulting partner and Board Member</div>
    <div class="abs" style="left:112px;top:160px;display:flex;gap:10px"><i style="width:16px;height:16px;background:#555;display:block"></i><i style="width:16px;height:16px;background:#555;display:block"></i><i style="width:16px;height:16px;background:#555;display:block"></i></div>
  </div>
  <div class="card" style="left:769px">
    <div class="photo" style="background:linear-gradient(180deg,#9ab0c6,#2a2f3a)" role="img" aria-label="Portrait of the advisor"></div>
    <div class="card-tag" style="bottom:48px">DANIEL RAVEL</div>
    <div class="card-role">ADVISOR</div>
  </div>
  <div class="arrows" style="left:1000px;top:565px">&#8592;&#8594;</div>
  <a class="abs view-more">View More</a>
</section>

<section class="sec stats">
  <div class="stat" style="left:130px"><b>2477</b><span>Finished Projects</span></div>
  <div class="stat" style="left:320px"><b>832</b><span>Happy Clients</span></div>
  <div class="stat" style="left:497px"><b>1858</b><span>Working Hours</span></div>
  <div class="stat" style="left:693px"><b>135</b><span>Satisfied Employees</span></div>
  <div class="stat" style="left:905px"><b>1858</b><span>Offices Worldwide</span></div>
</section>

<section class="sec testi">
  <div class="abs ghost">What Clients Say</div>
  <h2 class="abs heading">Our <span>Testimonials</span></h2>
  <div class="abs avatar" role="img" aria-label="Client portrait"></div>
  <p class="abs testi-name">Rene &amp; Sam Calder</p>
  <p class="abs sub">Harbrook delivered our road and drainage works ahead of schedule and within budget. The team was professional, safety minded and easy to work with from the first site meeting to final handover. We would gladly appoint them again for our next phase.</p>
  <div class="abs quote" style="left:180px;top:200px">&#8220;</div>
  <div class="abs quote" style="left:925px;top:230px">&#8221;</div>
  <div class="arrows" style="left:570px;top:380px">&#8592;&#8594;</div>
</section>

<section class="sec contact">
  <div class="abs ghost">Get In Touch</div>
  <h2 class="abs heading">Contact <span>Us</span></h2>
  <div class="col" style="left:150px">
    <h4>Contact Us</h4>
    <div class="row" style="margin-left:70px"><i></i>+27 61 555 0142</div>
    <div class="row" style="margin-left:70px"><i></i>info@harbrookplant.co.za</div>
    <div class="row" style="margin-left:70px"><i></i>086 555 0188</div>
  </div>
  <div class="divider" style="left:450px"></div>
  <div class="col" style="left:450px">
    <h4>Headoffice</h4>
    <p>PO Box 218, Northgate Ridge, 2301<br>9 Kestrel Crescent, Alderwood,<br>Kestrel Park, 2301</p>
  </div>
  <div class="divider" style="left:750px"></div>
  <div class="col" style="left:750px">
    <h4>Free State office</h4>
    <p>Suite 7, Marlow Square<br>Brookhaven 8812</p>
  </div>
</section>

<footer class="sec footer">
  <span class="abs" style="left:205px;top:10px">Privacy Policy</span>
  <span class="abs" style="left:430px;top:10px">Copyright &copy; 2018 Harbrook Plant and Civils. All rights reserved.</span>
  <div class="abs social" style="left:870px;top:6px"><i></i><i></i><i></i><i></i></div>
</footer>

</body>
</html>
```